We need a refreshed business card. Our company is a venture capital investment firm focused on investing in medical devices. Logo is attached. please also see our website www.velmoracapital.example

Target Market(s)

investors and potential investment targets

Industry/Entity Type

medical investments

Contact Information for Business Card

logo, name, title, email, phone, website, address,

Colors
0054AA
0677BA
7BADD7
CADEEF
E8F1F8
0094D4
00A9DD
6FCCEA
C7EBF8
E9F6FB
00AB8E
00BBA5
67D7C9
C6EFE9
E9F9F6

Requirements
Must have
• fresh modern design
Nice to have
• QR code leading to our linked in page, short description of what we do “Early Stage Medical Device Investors”

```html
<!DOCTYPE html>
<html lang="en">
<head>
<meta charset="utf-8">
<title>Velmora Health Ventures – Business Card</title>
<link rel="stylesheet" href="https://fonts.googleapis.com/css2?family=Hind:wght@400;600&family=Poppins:wght@400&display=swap">
<style>
  :root {
    --page: #ffffff;
    --card-light: #d5e8fc;
    --card-mid: #b8d8fc;
    --card-deep: #62acfb;
    --brand-blue: #0854a6;
    --brand-teal: #00ab8e;
    --ink: #333333;
    --rule: #3a3a3a;
  }
  * { box-sizing: border-box; margin: 0; padding: 0; }
  html, body {
    width: 1200px; height: 1200px; overflow: hidden;
    background: var(--page);
  }
  .canvas { position: relative; width: 1200px; height: 1200px; }
  .card {
    position: absolute; left: 136px; width: 935px; height: 534px;
    background: linear-gradient(150deg, var(--card-light) 0%, var(--card-light) 35%, var(--card-mid) 62%, var(--card-deep) 100%);
    overflow: hidden;
  }
  .card--front { top: 61px; }
  .card--back { top: 613px; }
  .card-texture {
    position: absolute; inset: 0;
    background: radial-gradient(ellipse at 45% 50%, rgba(167, 221, 236, 0.35), rgba(167, 221, 236, 0) 60%);
  }
  .wordmark {
    position: absolute;
    font-family: "Hind", sans-serif; font-weight: 600;
    color: var(--brand-blue); line-height: 1; white-space: nowrap;
  }
  .card--front .wordmark {
    left: 0; right: 0; top: 140px; text-align: center;
    font-size: 190px; letter-spacing: -2px;
  }
  .front-name {
    position: absolute; left: 0; right: 0; top: 418px; text-align: center;
    font-family: "Hind", sans-serif; font-weight: 400;
    font-size: 46px; color: var(--ink); line-height: 1; letter-spacing: 1px;
  }
  .card--back .wordmark {
    left: 33px; top: 218px; font-size: 118px; letter-spacing: -1px;
  }
  .divider {
    position: absolute; left: 492px; top: 149px; width: 2px; height: 235px;
    background: var(--rule);
  }
  .company-name {
    position: absolute; left: 561px; top: 84px;
    font-family: "Hind", sans-serif; font-weight: 400;
    font-size: 40px; line-height: 46px; letter-spacing: 5px;
    color: var(--ink); text-transform: uppercase;
  }
  .contact-list { list-style: none; }
  .contact {
    position: absolute; left: 515px; right: 20px;
    display: flex; align-items: flex-start;
    font-family: "Poppins", sans-serif; font-size: 22px; line-height: 32px;
    color: var(--ink); white-space: nowrap;
  }
  .contact-icon {
    flex: none; width: 30px; height: 30px; margin-right: 14px; margin-top: 1px;
  }
  .contact--phone { top: 252px; }
  .contact--address { top: 292px; }
  .contact--email { top: 360px; }
  .address-line2 { display: block; padding-left: 75px; }
</style>
</head>
<body>
<main class="canvas">

  <section class="card card--front" aria-label="Card front">
    <div class="card-texture" role="img" aria-label="Soft faint heartbeat-line background decoration"></div>
    <div class="wordmark">Velmora</div>
    <p class="front-name">VELMORA HEALTH VENTURES</p>
  </section>

  <section class="card card--back" aria-label="Card back">
    <div class="card-texture" role="img" aria-label="Soft faint heartbeat-line background decoration"></div>
    <div class="wordmark">Velmora</div>
    <div class="divider"></div>
    <h1 class="company-name">Velmora<br>Health<br>Ventures</h1>
    <ul class="contact-list">
      <li class="contact contact--phone">
        <svg class="contact-icon" viewBox="0 0 32 32" aria-hidden="true">
          <circle cx="16" cy="16" r="16" fill="var(--brand-teal)"/>
          <rect x="11" y="7" width="10" height="18" rx="2" fill="none" stroke="#fff" stroke-width="2"/>
          <circle cx="16" cy="21.5" r="1.2" fill="#fff"/>
        </svg>
        <span>214-555-0187</span>
      </li>
      <li class="contact contact--address">
        <svg class="contact-icon" viewBox="0 0 32 32" aria-hidden="true">
          <circle cx="16" cy="16" r="16" fill="var(--brand-teal)"/>
          <path d="M16 7a6 6 0 0 0-6 6c0 4.5 6 10 6 10s6-5.5 6-10a6 6 0 0 0-6-6z" fill="none" stroke="#fff" stroke-width="1.8"/>
          <circle cx="16" cy="13" r="2" fill="#fff"/>
          <ellipse cx="16" cy="25" rx="5" ry="1.5" fill="none" stroke="#fff" stroke-width="1.3"/>
        </svg>
        <span>88 Larkspur Row, Suite 612<span class="address-line2">Dallas, TX 75201</span></span>
      </li>
      <li class="contact contact--email">
        <svg class="contact-icon" viewBox="0 0 32 32" aria-hidden="true">
          <circle cx="16" cy="16" r="16" fill="var(--brand-teal)"/>
          <path d="M8 13l8-5 8 5v10H8z" fill="#fff"/>
          <path d="M8 13l8 5 8-5" fill="none" stroke="var(--brand-teal)" stroke-width="1.5"/>
        </svg>
        <span>info@velmoracapital.example</span>
      </li>
    </ul>
  </section>

</main>
</body>
</html>
```